Business Card Design

I am after a business card design to be made for my pet care business in Darwin, Northern Territory Australia called Merrily Mutts. I am a certified canine trainer and offer training classes from puppy love class, basic obedience classes, intermediate classes, private lessons, mobile dog wash and grooming and pet minding. I currently have a logo that I would like used on the card that incorporates different shades of orange with the writing in black. I really want my card to stand out from the rest and look professional, easy to read with 'the edge' factor. Im thinking both sides printed on with contact details on one side and services provided on the back
Updates

Thank you all so much for your time. I am overwhelmed with designs as they are all 

really great. My business partner and myself have shortlisted a few that really caught our eye and
Will update as soon as we decide. 

Once again thank you to you all for your great designs :)

Industry/Entity Type

Training

Contact Information for Business Card

Merrily Mutts
merrilymutts@postlark.example
merrilymutts.example.au
0437260000
pet minding
Puppy classes
basic obedience classes
intermediate obedience classes
private lessons
mobile dog wash and grooming
certified dog trainer
CDTQ certified
Police checked
fully insured
honest
reliable
find us on facebook www.socialnook.example/merrilymutts

Requirements
Must have
• My current logo either the stacked version or side by side - whatever works best and must include my services

```html
<!DOCTYPE html>
<html lang="en">
<head>
<meta charset="utf-8">
<title>Merrily Mutts – Business Card</title>
<link rel="stylesheet" href="https://fonts.googleapis.com/css2?family=Josefin+Sans:wght@300&family=Montserrat:wght@600&family=Dancing+Script:wght@500&display=swap">
<style>
  :root {
    --page: #ffffff;
    --card-light: #ffffff;
    --card-dark: #2b2a29;
    --gold: #c9961a;
    --gold-soft: #d9a935;
    --ink: #2b2a29;
    --text-light: #ffffff;
    --shadow: rgba(0, 0, 0, 0.28);
  }
  * { margin: 0; padding: 0; box-sizing: border-box; }
  html, body {
    width: 972px; height: 1200px; overflow: hidden;
    background: var(--page);
  }
  .canvas { position: relative; width: 972px; height: 1200px; }

  .card {
    position: absolute; left: 99px; width: 774px; height: 459px;
    border-radius: 34px; overflow: hidden;
    box-shadow: 0 6px 22px var(--shadow);
  }

  /* Front */
  .card--front { top: 90px; background: var(--card-light); }
  .brand-mark {
    position: absolute; left: 168px; top: 78px;
    width: 108px; height: 108px; border-radius: 50%;
    background: var(--gold-soft);
  }
  .brand-divider {
    position: absolute; left: 308px; top: 16px;
    width: 2px; height: 164px; background: var(--ink);
  }
  .brand-name {
    position: absolute; left: 340px; top: 38px;
    font-family: "Josefin Sans", sans-serif; font-weight: 300;
    font-size: 54px; line-height: 64px; letter-spacing: 2px;
    color: var(--ink); text-transform: uppercase;
  }
  .tagline {
    position: absolute; left: 0; right: 0; top: 176px;
    text-align: center;
    font-family: "Dancing Script", cursive; font-weight: 500;
    font-size: 48px; color: var(--ink);
  }
  .gold-band { position: absolute; left: 0; right: 0; height: 10px; background: var(--gold); }
  .card--front .gold-band { top: 246px; }
  .contact-panel {
    position: absolute; left: 0; right: 0; top: 259px; bottom: 0;
    background: var(--card-dark);
  }
  .contact-list { list-style: none; position: absolute; left: 180px; top: 14px; }
  .contact-list li {
    display: flex; align-items: center; height: 41px;
    font-family: "Montserrat", sans-serif; font-weight: 600;
    font-size: 21px; color: var(--text-light);
  }
  .contact-icon { width: 24px; height: 24px; margin-right: 20px; flex: none; }

  /* Back */
  .card--back { top: 640px; background: var(--card-dark); }
  .services-title {
    position: absolute; left: 0; right: 0; top: 18px; text-align: center;
    font-family: "Montserrat", sans-serif; font-weight: 600;
    font-size: 22px; color: var(--gold);
  }
  .services-list {
    list-style: none; position: absolute; top: 56px;
    font-family: "Montserrat", sans-serif; font-weight: 600;
    font-size: 19px; color: var(--text-light);
  }
  .services-list--left { left: 22px; }
  .services-list--right { left: 404px; top: 58px; }
  .services-list li { position: relative; height: 32.5px; padding-left: 27px; }
  .services-list li::before {
    content: ""; position: absolute; left: 4px; top: 8px;
    width: 7px; height: 7px; border-radius: 50%; background: var(--gold-soft);
  }
  .card--back .gold-band { top: 201px; }
  .photo-area {
    position: absolute; left: 0; right: 0; top: 211px; bottom: 0;
    background: linear-gradient(180deg, #8fa06a 0%, #b9b3a3 40%, #d8d3ca 70%, #cfc9bf 100%);
  }
</style>
</head>
<body>
<main class="canvas">

  <section class="card card--front" aria-label="Card front">
    <div class="brand-mark"></div>
    <div class="brand-divider"></div>
    <div class="brand-name">Merrily<br>Mutts</div>
    <p class="tagline">“It’s merry, to be a mutt”</p>
    <div class="gold-band"></div>
    <div class="contact-panel">
      <ul class="contact-list">
        <li>
          <svg class="contact-icon" viewBox="0 0 24 24" fill="none" stroke="#fff" stroke-width="1.6">
            <rect x="6" y="2.5" width="12" height="19" rx="2"/><line x1="11" y1="18.5" x2="13" y2="18.5"/>
          </svg>0437260000</li>
        <li>
          <svg class="contact-icon" viewBox="0 0 24 24" fill="none" stroke="#fff" stroke-width="1.6">
            <rect x="3" y="6" width="18" height="12"/><polyline points="3,6 12,13 21,6"/>
          </svg>merrilymutts@postlark.example</li>
        <li>
          <svg class="contact-icon" viewBox="0 0 24 24" fill="none" stroke="#fff" stroke-width="1.4">
            <circle cx="12" cy="12" r="9"/><ellipse cx="12" cy="12" rx="4" ry="9"/><line x1="3" y1="12" x2="21" y2="12"/><line x1="12" y1="3" x2="12" y2="21"/>
          </svg>www.merrilymutts.example.au</li>
        <li>
          <svg class="contact-icon" viewBox="0 0 24 24">
            <rect x="2" y="2" width="20" height="20" rx="3" fill="#4a6aa8"/>
          </svg>www.socialnook.example/merrilymutts</li>
      </ul>
    </div>
  </section>

  <section class="card card--back" aria-label="Card back">
    <h2 class="services-title">Services provided:</h2>
    <ul class="services-list services-list--left">
      <li>Pet minding</li>
      <li>Puppy classes</li>
      <li>Basic obedience classes</li>
      <li>Intermediate obedience classes</li>
    </ul>
    <ul class="services-list services-list--right">
      <li>Private lessons</li>
      <li>Mobile dog wash and grooming</li>
      <li>Certified dog trainer</li>
      <li>CDTQ certified Police</li>
    </ul>
    <div class="gold-band"></div>
    <div class="photo-area" role="img" aria-label="Photo of a walker leading several leashed dogs along a park footpath"></div>
  </section>

</main>
</body>
</html>
```